Bref créative
Stationery for HR Consultancy
Business card, letterhead & compliment slip
Use same font as used in my logo
Century Gothic
Professional
Rosalind Ashcombe, FMPSB
Managing Consultant
Cambridgeshire
United Kingdom
rashcombe@VelmoreCS.example
www.VelmoreCS.example
Coloured logo on business card front. open to your suggestions for other stationery.
the purple is the primary brand colour. Green is the accent colour.
the logo colour variations that are available and colour/font descriptions are attached.
i'll provide feedback to help steer the designs if needed.
Logo with text on the card reverse. I would consider a white on purple/green background (brand colours) on the reverse, as well as the coloured logo on white background.
White background on the front of card.
letterhead text positions

```html
<!DOCTYPE html>
<html lang="en">
<head>
<meta charset="utf-8">
<title>VelmoreCS Business Card</title>
<link href="https://fonts.googleapis.com/css2?family=Questrial&family=Cinzel:wght@400;600&display=swap" rel="stylesheet">
<style>
  :root {
    --brand-purple: #5a1f74;
    --brand-purple-light: #8a3aa8;
    --brand-purple-deep: #3f1254;
    --brand-green: #6fb63a;
    --ink: #5b5b5b;
    --card-white: #ffffff;
    --backdrop: #e9e9ea;
  }
  * { box-sizing: border-box; margin: 0; padding: 0; }
  html, body {
    width: 1200px; height: 895px; overflow: hidden;
    background: var(--backdrop);
  }
  .canvas { position: relative; width: 1200px; height: 895px; }

  .card {
    position: absolute;
    width: 580px; height: 330px;
    box-shadow: 0 14px 30px rgba(0,0,0,.18);
  }

  /* Reverse of the card */
  .card-back {
    left: 560px; top: 80px;
    border: 9px solid var(--brand-green);
    background: radial-gradient(ellipse at 45% 40%, var(--brand-purple-light) 0%, var(--brand-purple) 55%, var(--brand-purple-deep) 100%);
  }
  .back-brand {
    position: absolute; left: 0; right: 0; top: 118px;
    display: flex; align-items: center; justify-content: center; gap: 14px;
  }
  .brand-dot { width: 22px; height: 22px; border-radius: 50%; }
  .back-brand .brand-dot { background: var(--card-white); }
  .back-brand .brand-name {
    font-family: "Questrial", sans-serif;
    font-size: 40px; color: var(--card-white);
  }
  .back-web {
    position: absolute; left: 28px; bottom: 24px;
    font-family: "Cinzel", serif; font-size: 15px;
    letter-spacing: 4px; color: var(--card-white);
  }

  /* Front of the card */
  .card-front {
    left: 60px; top: 470px;
    border: 11px solid var(--brand-purple);
    background: var(--card-white);
  }
  .front-brand {
    position: absolute; left: 34px; top: 34px;
    display: flex; align-items: center; gap: 12px;
  }
  .front-brand .brand-dot { background: var(--brand-purple); }
  .front-brand .brand-name {
    font-family: "Questrial", sans-serif;
    font-size: 40px; color: var(--brand-purple);
  }
  .tagline {
    position: absolute; left: 68px; top: 86px;
    font-family: "Questrial", sans-serif; color: var(--brand-green);
    line-height: 1.25;
  }
  .tagline .line-main { font-size: 15px; }
  .tagline .line-sub { font-size: 13px; font-style: italic; padding-left: 60px; }

  .person {
    position: absolute; left: 232px; top: 140px;
    font-family: "Cinzel", serif; color: var(--ink);
  }
  .person .name { font-size: 17px; letter-spacing: .5px; color: var(--brand-purple); }
  .person .role { font-size: 12px; letter-spacing: .5px; line-height: 1.45; }

  .location {
    position: absolute; left: 34px; bottom: 38px;
    font-family: "Cinzel", serif; font-size: 12px;
    color: var(--ink); line-height: 1.5;
  }
  .contact {
    position: absolute; left: 232px; bottom: 30px;
    font-family: "Cinzel", serif; font-size: 11.5px;
    color: var(--ink); line-height: 1.55; list-style: none;
  }
  .contact li { display: flex; align-items: center; gap: 7px; }
  .contact svg { width: 10px; height: 10px; fill: var(--brand-purple); flex: none; }
</style>
</head>
<body>
<main class="canvas">

  <section class="card card-back" aria-label="Card reverse">
    <div class="back-brand">
      <span class="brand-dot"></span>
      <span class="brand-name">VelmoreCS</span>
    </div>
    <p class="back-web">WWW.VELMORECS.EXAMPLE</p>
  </section>

  <section class="card card-front" aria-label="Card front">
    <div class="front-brand">
      <span class="brand-dot"></span>
      <span class="brand-name">VelmoreCS</span>
    </div>
    <div class="tagline">
      <p class="line-main">People Management Consultants</p>
      <p class="line-sub">Putting business needs first</p>
    </div>

    <div class="person">
      <p class="name">Rosalind Ashcombe</p>
      <p class="role">Chartered FMPSB</p>
      <p class="role">Managing Consultant</p>
    </div>

    <div class="location">
      <p>Cambridgeshire</p>
      <p>United Kingdom</p>
    </div>

    <ul class="contact">
      <li><svg viewBox="0 0 10 10"><path d="M2 0.5l2 2-1 1.2a6 6 0 0 0 3.3 3.3l1.2-1 2 2-1.5 1.5C4 9 1 6 .5 2z"/></svg>01223 555 018</li>
      <li><svg viewBox="0 0 10 10"><rect x="2.5" y="0" width="5" height="10" rx="1"/></svg>07700 900 142</li>
      <li><svg viewBox="0 0 10 10"><path d="M0 2h10v6H0zM0 2l5 3.5L10 2" stroke="#fff" stroke-width=".8"/></svg>rashcombe@VelmoreCS.example</li>
      <li><svg viewBox="0 0 10 10"><circle cx="5" cy="5" r="4.5"/></svg>www.VelmoreCS.example</li>
    </ul>
  </section>

</main>
</body>
</html>
```